Design my site www.briefmarkpost.com

So here is what I am thinking in terms of design:

https://plenvo.com

https://www.skylarkjetways.com

http://quillweekly.com/harbor-tower-plaza/

I want the theme to be white and blue (royal blue). I attached a paint picture of what I would like the site to look like in terms of placing the text. Generally, what I like about the sites above is that they are simple, you can navigate easily and have some kind of idea of what's going on by looking at the center (picture and motto). Let's establish a clear understanding of how the functional part of the site would look like. Please see the picture attached.

I want to keep it simple: On top would be the Name 'BRIEFMARK post", somewhere to the right on top on the page would be 'Sign in" button.

In the center would be a picture (maybe a video) with the Motto (on top of it all in capital) OBSERVE NAVIGATE DECIDE and below would be the "sign up now"

Below the picture (like on quillweekly.com site) or to the left on top of the page would be "About Us', "Press" "Contact Us' buttons.

Then once the user gets to his page his got 3 tabs " Press Headlines", "Events", " Briefings".

we would keep the same format I only have on the site, but separate for every Tab.

I do not want the user to get distracted. I also want him to be able to access the page though mobile phone and be able to get automatic updates just like Zentro Pings without having to sign in daily.

The landing page must be minimalist yet with business/corporate feel where users can navigate easily and a "what you see is what you get" approach. You want an image or video (personally I prefer the video.. it does capture the users attention instantly, as long as it is an interesting video), with your taglines in it.

Sections available to public: About Us, Contact Us, Landing Page with Signup Option

Private: Public Sections + User Account Page, Tabs for (Events, Press Headlines, Briefings)

Target Market(s)

PR/media monitoring/diplomatic community

Coding

Coded - Design and coding required

Number of Pages Required

1 page

Font styles to use
Serif
Sans Serif

Colors
0255a3
ec1f27

Requirements
Must have
• a simple landing page, that is user friendly.
Nice to have
• a video with the explanation of how to navigate the site
Should not have
• too many colors, graphs etc.

```html
<!DOCTYPE html>
<html lang="en">
<head>
<meta charset="utf-8">
<title>BRIEFMARK post</title>
<link rel="stylesheet" href="https://fonts.googleapis.com/css2?family=Michroma&family=Open+Sans:wght@400;700&family=Poppins:wght@400&display=swap">
<style>
  :root {
    --royal-blue: #0255a3;
    --menu-blue: rgba(34, 88, 156, 0.85);
    --menu-divider: rgba(255, 255, 255, 0.12);
    --white: #ffffff;
    --sky-top: #23406e;
    --sky-mid: #4c6587;
    --sky-haze: #8a8f98;
    --city-light: #a88a6a;
    --city-warm: #8a6446;
    --city-deep: #4a4034;
    --river: #5d7186;
    --trees: #4d5a2e;
    --roof: #a0593c;
    --overlay: rgba(10, 20, 38, 0.34);
  }
  * { box-sizing: border-box; margin: 0; padding: 0; }
  html, body { width: 1200px; height: 600px; overflow: hidden; }
  body { font-family: "Open Sans", Arial, sans-serif; color: var(--white); }

  .hero {
    position: relative;
    width: 1200px;
    height: 600px;
    overflow: hidden;
  }
  .hero-backdrop {
    position: absolute;
    inset: 0;
    background:
      radial-gradient(ellipse 260px 240px at 60px 520px, var(--river) 0%, rgba(93,113,134,0) 100%),
      radial-gradient(ellipse 300px 160px at 1080px 560px, var(--trees) 0%, rgba(77,90,46,0) 100%),
      radial-gradient(ellipse 260px 120px at 1000px 470px, var(--roof) 0%, rgba(160,89,60,0) 100%),
      radial-gradient(ellipse 420px 200px at 380px 440px, var(--city-light) 0%, rgba(168,138,106,0) 100%),
      linear-gradient(180deg, var(--sky-top) 0%, var(--sky-mid) 26%, var(--sky-haze) 38%, var(--city-light) 46%, var(--city-warm) 66%, var(--city-deep) 100%);
  }
  .hero-backdrop::after {
    content: "";
    position: absolute;
    inset: 0;
    background: var(--overlay);
  }

  .sign-in {
    position: absolute;
    left: 922px;
    top: 38px;
    width: 117px;
    height: 33px;
    border: 1px solid var(--white);
    color: var(--white);
    font-weight: 700;
    font-size: 15px;
    letter-spacing: 0.3px;
    text-decoration: none;
    display: flex;
    align-items: center;
    justify-content: center;
  }

  .site-menu {
    position: absolute;
    left: 162px;
    top: 99px;
    width: 162px;
    list-style: none;
  }
  .site-menu li {
    height: 45px;
    background: var(--menu-blue);
    border-bottom: 1px solid var(--menu-divider);
  }
  .site-menu li.is-active { background: var(--royal-blue); }
  .site-menu a {
    display: flex;
    align-items: center;
    height: 100%;
    padding-left: 17px;
    font-family: "Poppins", Arial, sans-serif;
    font-size: 11.5px;
    color: var(--white);
    text-decoration: none;
    letter-spacing: 0.2px;
  }

  .hero-content {
    position: absolute;
    left: 0;
    right: 0;
    top: 195px;
    text-align: center;
  }
  .brand {
    display: inline-flex;
    align-items: center;
    gap: 8px;
    height: 20px;
    font-family: "Open Sans", Arial, sans-serif;
    font-weight: 700;
    font-size: 16px;
    color: var(--white);
    letter-spacing: 0.5px;
  }
  .brand-mark {
    width: 10px;
    height: 10px;
    background: var(--white);
  }
  .motto {
    margin-top: 28px;
    height: 31px;
    line-height: 31px;
    font-family: "Michroma", Arial, sans-serif;
    font-size: 23.5px;
    font-weight: 400;
    -webkit-text-stroke: 1.1px var(--white);
    letter-spacing: 0.4px;
  }
  .intro {
    margin-top: 17px;
    font-size: 15.4px;
    line-height: 22px;
  }
  .sign-up {
    display: inline-flex;
    align-items: center;
    justify-content: center;
    margin-top: 34px;
    width: 152px;
    height: 43px;
    background: var(--white);
    color: var(--royal-blue);
    font-weight: 700;
    font-size: 14px;
    letter-spacing: 0.3px;
    text-decoration: none;
  }
</style>
</head>
<body>
  <header class="hero">
    <div class="hero-backdrop" role="img" aria-label="Aerial photograph of a European city at sunset with a river, a tall TV tower, warm rooftops and trees under a blue sky"></div>

    <a class="sign-in" href="#">SIGN IN</a>

    <nav>
      <ul class="site-menu">
        <li class="is-active"><a href="#">ABOUT US</a></li>
        <li><a href="#">PRESS</a></li>
        <li><a href="#">CONTACT US</a></li>
      </ul>
    </nav>

    <div class="hero-content">
      <div class="brand"><span class="brand-mark"></span>BRIEFMARK post</div>
      <h1 class="motto">OBSERVE NAVIGATE DECIDE</h1>
      <p class="intro">This is Draftwell's version&nbsp; of Lorem Ipsum. Proin gravida nibh vel velit auctor aliquet.<br>Aenean sollicitudin, lorem quis bibendum auctor,</p>
      <a class="sign-up" href="#">SIGN UP NOW</a>
    </div>
  </header>
</body>
</html>
```